Web Design Project

This as the foundation http://lunorbix.com/demo_viewer/index.php?theme=velquistwp

Site needs to have a glossy black background with white text…..Extremely modern with a few flares of ravelle 6 style but nothing too off the wall, easily understood.

Here are some other reference sites and likes and dislikes that will help: (Probably overkill but we are looking for a cutting edge New York / LA Style )

http://www.torvikandcolb.com

Like- The black background with white font is very eye catching and clean. Love the contrast. Black is a great background for photographs and videos

http://samuelvorne.com

Like- Clean homepage, black and white color scheme works well.

http://douglaswhitcanephotography.com

Like- Nice Menu, nice B and W contrast

http://www.qkv.com

Like- Like the Menu. Clean and easy.

http://www.saffelmont.com

Like- Contrast of white background with black font.

Like- Slide show of stills (but should be able to click images to go to video. We’d also like the name of the project)

Like- Drop down menu allows for customer to find service they need without going through all services.

Like- Tells you work that they do right next to the logo.

Dislike- Too much information on homepage. Too much scrolling.

http://www.corbelvanestudios.com

Like- High Res images on home page

Like - The About Me is on homepage and speaks to potential customer directly. “We create award-winning videos for companies like yours.”

Like- Blog is updated with new projects they do. And short, visual entries

Like- “Work” section stands out from website. The background fades to light grey and white when you click on “work” so that the portfolio stands out more. Makes color look more vivid

Like- Black and white color scheme with grey header

http://www.fennwick748.com

Like- High Res images on home page pointing to projects

Like- Photograph as background, changes with different links. So work is always showcased and creates contrast. Information is laid over a barely translucent background, which is laid over the picture.

Like- They have a good Attitude about quality of their product

http://www.quillbramt.net

Like- First thing you see when open page is a clear big statement about what they do, said in a catchy way. They have a Tagline.

http://plimsworthdesign.com

Like- How work is categorized. Client list has links, which take you to their Client page with all their work grouped together. Nice flow and organization shows client relationships. And nice descriptions of what the job was and how it was executed… Way too wordy at times though

http://www.marivantphotography.com

Like- The homepage is very clean and accessible. Love the color scheme and how Logo is centered between the links.

Of the four designs we have gotten EVERY SINGLE ONE has been a template STOLEN from another site. We are paying for ORIGINAL design. Not copies and templates. Please ONLY submit original designs

```html
<!DOCTYPE html>
<html lang="en">
<head>
<meta charset="utf-8">
<title>Velvetone Productions</title>
<link rel="stylesheet" href="https://fonts.googleapis.com/css2?family=Anton&family=Open+Sans:wght@400;600;700&display=swap">
<style>
  :root {
    --page: #f7f7f7;
    --ink: #111111;
    --black: #000000;
    --band: #0b0b0b;
    --white: #ffffff;
    --muted: #b9b9b9;
    --heading-grey: #3a3a3a;
    --rule: #dddddd;
    --icon: #a8a8a8;
    --accent: #1aa6e0;
    --footer-text: #5a5a5a;
  }
  * { box-sizing: border-box; margin: 0; padding: 0; }
  html, body { width: 1200px; height: 1000px; overflow: hidden; }
  body { position: relative; background: var(--page); font-family: "Open Sans", Arial, sans-serif; color: var(--ink); }
  .abs { position: absolute; }
  .display { font-family: "Anton", Impact, sans-serif; text-transform: uppercase; font-weight: 400; }

  .top-rule { left: 0; top: 0; width: 1200px; height: 4px; background: var(--black); }

  .brand { left: 300px; top: 40px; display: flex; align-items: center; gap: 10px; }
  .brand-mark { width: 26px; height: 26px; border: 2px solid var(--ink); }
  .brand-name { font-size: 20px; font-weight: 600; color: var(--ink); letter-spacing: 0.5px; }

  .search { left: 718px; top: 46px; width: 161px; height: 23px; border: 1px solid #d6d6d6; background: #f2f2f2; font-size: 8px; color: #777; padding: 6px 10px; }
  .search svg { position: absolute; right: 10px; top: 6px; }
  .social { left: 814px; top: 80px; display: flex; gap: 3px; }
  .social span { width: 10px; height: 10px; background: var(--icon); border-radius: 2px; display: block; }

  .hero { left: 0; top: 119px; width: 1200px; height: 283px; background: linear-gradient(180deg, #121212, #050505); }
  .main-nav { left: 295px; top: 142px; list-style: none; }
  .main-nav li { font-size: 17px; line-height: 18.6px; color: var(--white); }
  .main-nav li.current { color: #6d6d6d; }

  .video { left: 494px; top: 137px; width: 385px; height: 248px; background: radial-gradient(ellipse at 55% 40%, #a8805e 0%, #6a4a36 35%, #23303f 75%, #0e1622 100%); }
  .video-title { left: 517px; top: 159px; display: flex; gap: 4px; }
  .video-thumb { width: 38px; height: 37px; background: #111; border: 1px solid #444; }
  .video-title .t1 { background: #111; color: var(--accent); font-size: 11px; font-weight: 700; padding: 0 4px; line-height: 14px; display: inline-block; }
  .video-title .t2 { background: #111; color: #ddd; font-size: 7px; padding: 0 4px; line-height: 12px; display: inline-block; margin-top: 2px; }
  .video-title .t2 b { color: var(--accent); font-weight: 400; }
  .side-btn { left: 836px; width: 27px; height: 22px; background: rgba(0,0,0,.8); border-radius: 2px; color: #fff; font-size: 5px; text-align: center; padding-top: 13px; font-weight: 700; }
  .side-btn::before { content: ""; position: absolute; left: 9px; top: 3px; width: 9px; height: 8px; background: #fff; border-radius: 2px; }
  .player { left: 518px; top: 339px; width: 336px; height: 22px; background: rgba(0,0,0,.75); border-radius: 2px; }
  .player .track { position: absolute; left: 53px; top: 9px; width: 212px; height: 6px; background: #444; }
  .player .track i { display: block; width: 60px; height: 6px; background: var(--accent); }
  .player .hd { position: absolute; left: 297px; top: 4px; font-size: 9px; font-weight: 700; color: var(--accent); font-style: italic; }

  .tagline { left: 0; top: 427px; width: 1180px; text-align: center; font-size: 20px; font-weight: 700; }
  .welcome { left: 295px; top: 468px; }
  .welcome .lead { font-size: 25px; color: var(--muted); line-height: 28px; font-family: "Open Sans", sans-serif; font-weight: 700; }
  .welcome .name { font-size: 28px; line-height: 29px; color: var(--heading-grey); }
  .divider { left: 481px; top: 470px; width: 1px; height: 100px; background: var(--rule); }
  .intro { left: 494px; top: 470px; width: 380px; font-size: 9.5px; line-height: 14px; }
  .intro strong { display: block; margin-bottom: 7px; }

  .section-title { font-size: 17px; color: var(--ink); }
  .section-title span { color: #c4c4c4; margin-left: 12px; }
  .card { top: 649px; width: 186px; height: 73px; }
  .card .label { position: absolute; left: 0; top: 37px; background: var(--black); color: #fff; font-size: 12px; padding: 2px 6px 2px 5px; line-height: 17px; }
  .arrow { top: 678px; }

  .post-thumb { width: 38px; height: 34px; top: 805px; }
  .post { top: 803px; width: 140px; }
  .post h3 { font-size: 12.5px; line-height: 14px; margin-bottom: 8px; }
  .post p { font-size: 9.5px; line-height: 14px; }
  .post p b { font-weight: 700; }

  .quote-box { left: 693px; top: 805px; width: 186px; height: 78px; background: #e2e2e2; padding: 6px; }
  .quote-box .inner { background: var(--black); width: 100%; height: 100%; color: #fff; display: flex; align-items: center; gap: 10px; padding-left: 14px; font-size: 17px; line-height: 16px; }

  .footer { left: 0; top: 917px; width: 1200px; height: 83px; background: var(--black); }
  .footer p { position: absolute; left: 295px; top: 24px; font-size: 8.5px; color: var(--footer-text); }
</style>
</head>
<body>
  <div class="abs top-rule"></div>

  <header>
    <div class="abs brand"><span class="brand-mark"></span><span class="brand-name">Velvetone Productions</span></div>
    <div class="abs search">Search Here...
      <svg width="9" height="9" viewBox="0 0 10 10"><circle cx="4" cy="4" r="3" fill="none" stroke="#666" stroke-width="1.5"/><line x1="6.2" y1="6.2" x2="9" y2="9" stroke="#666" stroke-width="1.6"/></svg>
    </div>
    <div class="abs social" aria-label="Social links"><span></span><span></span><span></span><span></span><span></span></div>
  </header>

  <section class="abs hero"></section>
  <ul class="abs main-nav display">
    <li class="current">Home</li><li>Services</li><li>Video Gallery</li><li>About Us</li><li>Contact Us</li><li>Show Reel</li><li>Actor Demo Reels</li><li>Video Blog</li><li>Client List</li><li>Client Testimonials</li><li>Photo Gallery</li><li>FAQ</li>
  </ul>

  <div class="abs video" role="img" aria-label="Video still: portrait of a woman in a fur hat against city lights"></div>
  <div class="abs video-title"><span class="video-thumb"></span><div><span class="t1">STYLE</span><br><span class="t2">from <b>Velvetone Productions</b></span></div></div>
  <div class="abs side-btn" style="top:158px">LIKE</div>
  <div class="abs side-btn" style="top:183px">LATER</div>
  <div class="abs side-btn" style="top:208px">SHARE</div>
  <div class="abs side-btn" style="top:233px">EMBED</div>
  <div class="abs player">
    <svg style="position:absolute;left:15px;top:5px" width="12" height="12" viewBox="0 0 12 12"><path d="M2 1 L11 6 L2 11 Z" fill="#fff"/></svg>
    <div class="track"><i></i></div>
    <svg style="position:absolute;left:271px;top:7px" width="22" height="8"><g fill="#1aa6e0"><rect x="0" width="2" height="8"/><rect x="3" width="2" height="8"/><rect x="6" width="2" height="8"/><rect x="9" width="2" height="8"/><rect x="12" width="2" height="8"/><rect x="15" width="2" height="8"/><rect x="18" width="2" height="8"/></g></svg>
    <span class="hd">HD</span>
    <svg style="position:absolute;left:318px;top:7px" width="8" height="8" viewBox="0 0 8 8"><path d="M0 0h3L0 3zM8 0v3L5 0zM0 8V5l3 3zM8 8H5l3-3z" fill="#fff"/></svg>
  </div>

  <h1 class="abs tagline">“We create award-winning videos for companies like yours.”</h1>
  <div class="abs welcome">
    <div class="lead">WELCOME TO</div>
    <div class="name display">Velvetone<br>Productions</div>
  </div>
  <div class="abs divider"></div>
  <div class="abs intro">
    <strong>We are Velvetone Production lorem ipsum dolor sit amet, consectetur adipiscing elit. Quisque posuere feugiat gravida. Sed fringilla velit vitae commodo condimentum</strong>
    Donec euismod laoreet lorem at auctor. Vestibulum nec laoreet ipsum. Nam neque felis, euismod sed diam ac, euismod interdum urna. Mauris tincidunt feugiat viverra. Pellentesque vehicula nunc ac luctus condimentum. Morbi id libero sed leo hendrerit bibendum. Pellentesque malesuada diam libero, eu elementum urna venenatis in.
  </div>

  <h2 class="abs section-title display" style="left:296px;top:608px">Featured Projects<span>View All</span></h2>
  <svg class="abs arrow" style="left:270px" width="11" height="16" viewBox="0 0 11 16"><path d="M9 1 L2 8 L9 15" fill="none" stroke="#333" stroke-width="3"/></svg>
  <div class="abs card" style="left:296px;background:linear-gradient(135deg,#6f6558,#2e2a26)" role="img" aria-label="Project still: two men in a studio"><span class="label display">Project Title Here..</span></div>
  <div class="abs card" style="left:494px;background:linear-gradient(135deg,#e9d3c0,#b8705a)" role="img" aria-label="Project still: glamour portrait of a woman"><span class="label display">Project Title Here..</span></div>
  <div class="abs card" style="left:693px;background:linear-gradient(135deg,#b07a3e,#1b1a26)" role="img" aria-label="Project still: man in sunglasses, warm backlight"><span class="label display">Project Title Here..</span></div>
  <svg class="abs arrow" style="left:893px" width="11" height="16" viewBox="0 0 11 16"><path d="M2 1 L9 8 L2 15" fill="none" stroke="#333" stroke-width="3"/></svg>

  <h2 class="abs section-title display" style="left:296px;top:764px">Latest Blog<span>Read More</span></h2>
  <div class="abs post-thumb" style="left:295px;background:linear-gradient(135deg,#c9806a,#6b3b2c)" role="img" aria-label="Blog thumbnail photo"></div>
  <article class="abs post" style="left:345px">
    <h3 class="display" style="text-transform:none">Sed et leo sollicitudin velit suscipit lacinia</h3>
    <p>Nam non adipiscing lectus. Quisque tempor nibh vel placerat posuere... <b>READ MORE</b></p>
  </article>
  <div class="abs post-thumb" style="left:493px;background:linear-gradient(135deg,#4f6f86,#1e2a33)" role="img" aria-label="Blog thumbnail photo"></div>
  <article class="abs post" style="left:543px">
    <h3 class="display" style="text-transform:none">Sed et leo sollicitudin velit suscipit lacinia</h3>
    <p>Nam non adipiscing lectus. Quisque tempor nibh vel placerat posuere... <b>READ MORE</b></p>
  </article>
  <div class="abs quote-box">
    <div class="inner display">
      <svg width="18" height="13" viewBox="0 0 18 13"><rect x="1" y="1" width="16" height="11" fill="none" stroke="#fff" stroke-width="1.6"/><path d="M1 1 L9 7 L17 1" fill="none" stroke="#fff" stroke-width="1.6"/></svg>
      <span>Contact Us<br>For a Free Quote</span>
    </div>
  </div>

  <footer class="abs footer"><p>Copyright © 2013 Velvetone Productions. All rights reserved.</p></footer>
</body>
</html>
```